"The Wandering Mentor", a Higher Ed blogger, would like a wordpress design

I would like a wordpress design for blogs written by "The Wandering Mentor." that can be easily expanded by me once the initial design is complete.

Here is context which I would like included on the Home/Welcome page: "I started The Wandering Mentor in 2021 to write about the practice of academic advising through the lens of horsemanship. After one year of developing skills as a brand new equestrian, I couldn’t help but notice the similarities between my vocation as an academic advisor and my avocation as a budding equestrian. I hope my musings about my journey in two very different fields will cultivate curiosity, widen your aperture and ignite academic advisors to take their practice to the next level. "

The wordpress will primarily have blogs by myself or guest bloggers writing about academic advising for advisors, but I may widen my audience to include students and families. I'd like to have readers submit questions that I can answer. Depending on interest, I may want to have a section on Horsemanship but that is not truly the focus of this site.

I'd like the feel of the site to be positive, fresh, modern (but not too wild), with the emphasis on Higher Ed/Academic Advising as opposed to equestrian pursuits. I don't want it to feel clunky and blocky like some sites that have to do with education. I'm hoping that readers will have some "aha" moments after reading some of the posts.

I have included my logo files

```html
<!DOCTYPE html>
<html lang="en">
<head>
<meta charset="utf-8">
<title>The Wandering Mentor</title>
<link href="https://fonts.googleapis.com/css2?family=Bebas+Neue&family=Noto+Serif:wght@400;600;700&family=Poppins:wght@300;400;500&display=swap" rel="stylesheet">
<style>
:root{
  --gold:#d3a35c;
  --gold-soft:#e2c08c;
  --ink:#1f1f1f;
  --body:#555;
  --muted:#8a8a8a;
  --cream:#f6eee3;
  --line:#e4e4e4;
  --footer:#1e1e1e;
  --white:#fff;
}
*{margin:0;padding:0;box-sizing:border-box}
html,body{width:1200px;height:5386px;overflow:hidden;background:var(--white)}
body{position:relative;font-family:'Poppins',sans-serif;color:var(--ink)}
.abs{position:absolute}
.serif{font-family:'Noto Serif',serif}
.photo{position:absolute;display:block}

/* header */
.brand{left:62px;top:14px;display:flex;align-items:center;gap:10px}
.brand-dot{width:22px;height:22px;border-radius:50%;background:var(--gold)}
.brand-name{font-family:'Noto Serif',serif;font-weight:600;font-size:15px;color:var(--gold);line-height:1.2;width:110px}
.nav{left:340px;top:38px;display:flex;gap:26px;font-size:12.5px;color:var(--ink)}
.search{left:1101px;top:27px;width:38px;height:38px;border:1.5px solid var(--ink);border-radius:50%}

/* hero */
.hero-photo{left:450px;top:119px;width:522px;height:522px;border-radius:50%;background:radial-gradient(circle at 50% 40%,#5b4a36 0%,#6f7a45 40%,#c9b98f 75%,#d8cdb6 100%)}
.hero-title{right:642px;top:268px;text-align:right;font-family:'Bebas Neue',sans-serif;font-size:53px;line-height:63px;letter-spacing:.5px;color:var(--ink);z-index:2}
.hero-title .accent{color:var(--gold)}
.btn{display:inline-block;background:var(--gold);color:var(--white);font-family:'Noto Serif',serif;font-weight:600;font-size:13px;letter-spacing:.5px;text-align:center;border-radius:22px}
.hero-btn{left:408px;top:468px;width:146px;height:38px;line-height:38px;z-index:2}
.slider-bars{left:1136px;top:335px;width:3px}
.slider-bars span{display:block;width:3px;height:20px;margin-bottom:12px;background:#2d3d55}
.slider-bars span.on{background:var(--gold)}
.social{left:1120px;top:584px;display:flex;flex-direction:column;gap:18px}
.social span{width:16px;height:16px;border:2px solid var(--gold);border-radius:50%}
.divider{left:0;top:711px;width:1200px;height:1px;background:var(--line)}

/* news */
.news-feature{left:61px;top:736px;width:449px;height:426px;background:linear-gradient(160deg,#3a3a36,#2a2a24 60%,#3b3a2c)}
.news-feature-label{left:61px;top:920px;width:449px;text-align:center;font-family:'Noto Serif',serif;font-weight:600;font-size:42px;color:var(--gold-soft)}
.news-item{position:absolute;left:533px;width:580px;height:125px}
.news-item .thumb{position:absolute;left:0;top:0;width:194px;height:125px}
.news-item .cat{position:absolute;left:230px;top:4px;font-size:12px;color:var(--gold)}
.news-item h3{position:absolute;left:230px;top:30px;width:340px;font-family:'Noto Serif',serif;font-weight:700;font-size:15px;line-height:23px;color:var(--ink)}
.news-item .meta{position:absolute;left:230px;top:94px;font-size:11px;color:#555}
.news-item .meta i{display:inline-block;width:6px;height:6px;border-radius:50%;background:var(--ink);margin:0 12px 1px;vertical-align:middle}
.news-scroll{left:1137px;top:736px;width:1px;height:414px;background:var(--line)}
.news-scroll span{position:absolute;left:-1px;top:66px;width:3px;height:26px;background:var(--gold)}

/* events */
.section-title{font-family:'Noto Serif',serif;font-weight:600;color:var(--ink)}
.events-title{left:213px;top:1246px;font-size:60px;line-height:60px}
.events-rule{left:485px;top:1306px;width:418px;height:1px;background:var(--line)}
.arrow{top:1286px;width:40px;height:40px;border-radius:50%;border:1.5px solid var(--ink)}
.arrow.prev{left:919px;border-color:var(--gold-soft)}
.arrow.next{left:967px}
.arrow svg{position:absolute;left:12px;top:11px}
.event-photo{width:330px;height:224px}
.date-badge{position:absolute;width:62px;height:64px;background:#1c1c1c;color:var(--white);text-align:center;font-family:'Noto Serif',serif;z-index:2}
.date-badge b{display:block;font-size:27px;line-height:30px;margin-top:6px;font-weight:600}
.date-badge span{display:block;font-size:12px;font-weight:700;letter-spacing:.5px}
.event-text{position:absolute;width:360px}
.event-text .cat{font-size:12px;color:var(--gold);margin-bottom:10px}
.event-text h3{font-family:'Noto Serif',serif;font-weight:700;font-size:16px;line-height:24px;margin-bottom:10px}
.event-text p{font-size:10.5px;line-height:20px;color:var(--body);margin-bottom:16px}
.event-text .btn{width:146px;height:40px;line-height:40px}
.event-text.right{text-align:right}

/* welcome */
.welcome-band{left:0;top:2314px;width:690px;height:501px;background:var(--cream)}
.welcome-photo{left:690px;top:2314px;width:449px;height:501px;background:linear-gradient(180deg,#6d8a55 0%,#4a5d3a 45%,#7b6a55 75%,#3a4a6a 100%)}
.welcome-kicker{left:117px;top:2398px;font-family:'Noto Serif',serif;font-weight:700;font-size:13px}
.welcome-title{left:115px;top:2426px;font-size:46px;line-height:52px}
.welcome-text{left:115px;top:2548px;width:420px;font-size:10.5px;line-height:21px;color:var(--body)}
.welcome-mark{left:612px;top:2500px;width:150px;height:150px;border-radius:50%;background:var(--cream);display:flex;align-items:center;justify-content:center;text-align:center;font-family:'Noto Serif',serif;font-weight:600;font-size:16px;line-height:22px;color:var(--gold);padding:20px}

/* advice */
.advice-title{left:0;top:2880px;width:1200px;text-align:center;font-size:46px}
.advice-card{position:absolute;top:2983px;width:300px;text-align:center}
.advice-card .thumb{height:186px;width:100%}
.advice-card .badge{position:absolute;left:120px;top:156px;width:60px;height:60px;border-radius:50%;background:#1c1c1c;border:3px solid var(--white)}
.advice-card h3{margin-top:52px;font-family:'Noto Serif',serif;font-weight:700;font-size:15px}
.advice-card h4{font-family:'Noto Serif',serif;font-weight:400;font-size:15px;color:var(--gold);margin-top:2px}
.advice-card p{font-size:10.5px;line-height:20px;color:var(--body);margin:10px auto 0;width:240px}
.advice-card .rule{width:150px;height:2px;background:var(--gold);margin:30px auto 0}

/* horsemanship */
.horse-band{left:61px;top:3432px;width:1139px;height:449px;background:linear-gradient(90deg,#1d2a1a 0%,#2b3a24 45%,#4a5536 75%,#34402a 100%)}
.horse-title{left:123px;top:3618px;font-size:50px;color:var(--white);font-weight:600}
.horse-text{left:123px;top:3694px;width:440px;font-size:10.5px;line-height:21px;color:#e9e9e9}

/* gallery */
.gallery-title{left:0;top:3942px;width:1200px;text-align:center;font-size:46px}
.gallery{left:63px;top:4042px;width:1076px;height:481px;display:grid;grid-template-columns:repeat(4,1fr);grid-template-rows:repeat(2,1fr);gap:4px}
.gallery div{position:relative}
.gallery .tint{background:#d2ad70}
.gallery .tint svg{position:absolute;left:50%;top:50%;transform:translate(-50%,-50%)}

/* question */
.q-title{left:63px;top:4590px;font-size:46px}
.q-text{left:63px;top:4660px;width:480px;font-size:11px;line-height:21px;color:var(--body)}
.field{position:absolute;left:320px;width:522px;height:24px;border-bottom:1px solid #777;font-size:11px;color:var(--ink)}
.submit{left:316px;top:4955px;width:108px;height:40px;line-height:40px}

/* footer */
.footer{left:0;top:5073px;width:1200px;height:313px;background:var(--footer);color:var(--white)}
.f-brand{left:110px;top:5120px;width:150px;height:150px;border-radius:50%;border:2px solid var(--gold);display:flex;align-items:center;justify-content:center;text-align:center;font-family:'Noto Serif',serif;font-weight:600;font-size:16px;line-height:22px;color:var(--gold);padding:20px}
.f-social{left:142px;top:5285px;display:flex;gap:14px}
.f-social span{width:14px;height:14px;border:2px solid var(--gold);border-radius:50%}
.f-head{top:5118px;font-family:'Noto Serif',serif;font-weight:700;font-size:14px}
.f-list{left:340px;top:5156px;font-size:10.5px;line-height:22px;list-style:none;color:#ddd}
.f-contact{left:612px;top:5156px;font-size:10.5px;line-height:28px;color:#ddd}
.f-contact div{display:flex;align-items:center;gap:12px}
.f-news{left:886px;top:5155px;width:250px;font-size:10.5px;line-height:21px;color:#ddd}
.f-input{left:886px;top:5210px;width:253px;height:38px;border-radius:20px;background:var(--white);color:#555;font-size:10.5px;line-height:38px;padding-left:16px}
.f-input span{position:absolute;right:4px;top:4px;width:30px;height:30px;border-radius:50%;background:var(--gold)}
.f-input svg{position:absolute;left:8px;top:8px}
.copy{left:0;top:5354px;width:1200px;text-align:center;font-size:10.5px;color:#ddd}
.copy em{font-style:normal;color:var(--gold)}
</style>
</head>
<body>

<!-- header -->
<div class="abs brand"><span class="brand-dot"></span><span class="brand-name">The Wandering Mentor</span></div>
<nav class="abs nav"><span>News</span><span>Events</span><span>Gallery</span><span>Advise</span><span>Horsemanship</span><span>Dressage</span><span>Contact Us</span></nav>
<div class="abs search"><svg width="38" height="38" viewBox="0 0 38 38"><circle cx="17.5" cy="17.5" r="6" fill="none" stroke="#1f1f1f" stroke-width="1.6"/><line x1="22" y1="22" x2="25.5" y2="25.5" stroke="#1f1f1f" stroke-width="1.6" stroke-linecap="round"/></svg></div>

<!-- hero -->
<div class="photo hero-photo" role="img" aria-label="Rider on a dark horse clearing a blue and white show jump"></div>
<h1 class="abs hero-title">A place for our thoughts<br>fears, finds, fads<br><span class="accent">obsessions and opinions</span></h1>
<span class="abs btn hero-btn">KNOW MORE</span>
<div class="abs slider-bars"><span></span><span></span><span class="on"></span><span></span></div>
<div class="abs social" aria-label="Social links"><span></span><span></span><span></span></div>
<div class="abs divider"></div>

<!-- news -->
<div class="photo news-feature" role="img" aria-label="Rider jumping a log fence in a field at dusk"></div>
<div class="abs news-feature-label">News</div>
<article class="news-item" style="top:736px">
  <div class="photo thumb" role="img" aria-label="People working with a horse on a sandy track" style="background:linear-gradient(180deg,#7ea0c4,#b9b4a2 55%,#8b7a5f)"></div>
  <div class="cat">Academic Advising</div>
  <h3>Lorem Ipsum has been the industry's standard dummy text ever!</h3>
  <div class="meta">September 10, 2021<i></i>5 min read</div>
</article>
<article class="news-item" style="top:886px">
  <div class="photo thumb" role="img" aria-label="Rider celebrating beside a horse at sunset" style="background:linear-gradient(180deg,#e39a4a,#c4692c 55%,#7a3d1d)"></div>
  <div class="cat">Equestrian</div>
  <h3>Lorem Ipsum has been the industry's standard dummy text ever!</h3>
  <div class="meta">September 10, 2021<i></i>5 min read</div>
</article>
<article class="news-item" style="top:1037px">
  <div class="photo thumb" role="img" aria-label="Trainer lunging a rearing horse on grass" style="background:linear-gradient(180deg,#8ab6d8,#6f9a4c 55%,#3e5f2b)"></div>
  <div class="cat">Academic Advising</div>
  <h3>Lorem Ipsum has been the industry's standard dummy text ever!</h3>
  <div class="meta">September 10, 2021<i></i>5 min read</div>
</article>
<div class="abs news-scroll"><span></span></div>

<!-- events -->
<h2 class="abs section-title events-title">Latest<br>Events</h2>
<div class="abs events-rule"></div>
<div class="abs arrow prev"><svg width="14" height="16" viewBox="0 0 14 16"><path d="M9 2 L4 8 L9 14" fill="none" stroke="#e2c08c" stroke-width="1.6"/></svg></div>
<div class="abs arrow next"><svg width="14" height="16" viewBox="0 0 14 16"><path d="M5 2 L10 8 L5 14" fill="none" stroke="#1f1f1f" stroke-width="1.6"/></svg></div>

<div class="date-badge" style="left:199px;top:1467px"><b>25</b><span>SEP</span></div>
<div class="photo event-photo" role="img" aria-label="Rider on a chestnut horse jumping a fence among trees" style="left:249px;top:1434px;background:linear-gradient(180deg,#9dbbd6,#5e7d3e 45%,#8a6a42 80%,#a88f6c)"></div>
<div class="event-text" style="left:640px;top:1455px">
  <div class="cat">Horsemanship</div>
  <h3>Lorem Ipsum has been the industry's<br>standard dummy text ever!</h3>
  <p>Lorem Ipsum has been the industry's standard dummy text<br>ever since the 1500s, when an unknown printer.</p>
  <span class="btn">BOOK EVENT</span>
</div>

<div class="event-text right" style="left:229px;top:1741px">
  <div class="cat">Horsemanship</div>
  <h3>Lorem Ipsum has been the industry's<br>standard dummy text ever!</h3>
  <p>Lorem Ipsum has been the industry's standard dummy text<br>ever since the 1500s, when an unknown printer.</p>
  <span class="btn">BOOK EVENT</span>
</div>
<div class="photo event-photo" role="img" aria-label="Rider on a bay horse in a green meadow" style="left:652px;top:1722px;background:linear-gradient(180deg,#7da84a,#5f8f35 60%,#4d7a2a)"></div>
<div class="date-badge" style="left:966px;top:1756px"><b>25</b><span>SEP</span></div>

<div class="date-badge" style="left:199px;top:2038px"><b>25</b><span>SEP</span></div>
<div class="photo event-photo" role="img" aria-label="Barrel racer turning a horse in a dusty arena below mountains" style="left:249px;top:2006px;background:linear-gradient(180deg,#a9c3dc,#7b8a8e 35%,#c3ab8a 60%,#b39873)"></div>
<div class="event-text" style="left:640px;top:2024px">
  <div class="cat">Equestrian</div>
  <h3>Lorem Ipsum has been the industry's<br>standard dummy text ever!</h3>
  <p>Lorem Ipsum has been the industry's standard dummy text<br>ever since the 1500s, when an unknown printer.</p>
  <span class="btn">BOOK EVENT</span>
</div>

<!-- welcome -->
<div class="abs welcome-band"></div>
<div class="photo welcome-photo" role="img" aria-label="Show jumper on a chestnut horse mid-leap over a rail"></div>
<div class="abs welcome-mark">The Wandering Mentor</div>
<div class="abs welcome-kicker">Welcome To</div>
<h2 class="abs section-title welcome-title">The Wandering<br>Mentor</h2>
<p class="abs welcome-text">I started The Wandering Mentor in 2021 to write about the practice of academic advising through the lens of horsemanship. After one year of developing skills as a brand new equestrian, I couldn't help but notice the similarities between my vocation as an academic advisor and my avocation as a budding equestrian. I hope my musings about my journey in two very different fields will cultivate curiosity, widen your aperture and ignite academic advisors to take their practice to the next level</p>

<!-- advice -->
<h2 class="abs section-title advice-title">Advice</h2>
<article class="advice-card" style="left:136px">
  <div class="photo thumb" role="img" aria-label="Bay horse in a warm-lit arena" style="position:relative;background:linear-gradient(180deg,#5a3c22,#8a5a30 50%,#c9a67a)"></div>
  <span class="badge"></span>
  <h3>Lorem Ipsum has been the typeing</h3><h4>Academic Advisor</h4>
  <p>Lorem Ipsum has been the industry's standard dummy text ever since the 1500s, when an unknown printer.</p>
  <div class="rule"></div>
</article>
<article class="advice-card" style="left:458px">
  <div class="photo thumb" role="img" aria-label="Rider standing beside a horse in blue light" style="position:relative;background:linear-gradient(180deg,#5d7fa8,#4f6079 50%,#6b5a46)"></div>
  <span class="badge"></span>
  <h3>Lorem Ipsum has been the typeing</h3><h4>Academic Advisor</h4>
  <p>Lorem Ipsum has been the industry's standard dummy text ever since the 1500s, when an unknown printer.</p>
  <div class="rule"></div>
</article>
<article class="advice-card" style="left:778px;width:286px">
  <div class="photo thumb" role="img" aria-label="Close view of a bridled horse outdoors" style="position:relative;background:linear-gradient(180deg,#c8d2de,#7a5a3e 55%,#4c3522)"></div>
  <span class="badge" style="left:113px"></span>
  <h3>Lorem Ipsum has been the typeing</h3><h4>Academic Advisor</h4>
  <p>Lorem Ipsum has been the industry's standard dummy text ever since the 1500s, when an unknown printer.</p>
  <div class="rule"></div>
</article>

<!-- horsemanship -->
<div class="photo horse-band" role="img" aria-label="Group of riders trotting away across a dark green field"></div>
<h2 class="abs section-title horse-title">Horsemanship</h2>
<p class="abs horse-text">Lorem Ipsum has been the industry's standard dummy text ever since the 1500s, when an unknown printer took a galley of type and scrambled it to make a type specimen book. It has survived not only five centuries, but also the leap into electronic typesetting, remaining essentially unchanged. It was popularised in the 1960s.</p>

<!-- gallery -->
<h2 class="abs section-title gallery-title">Our Gallery</h2>
<div class="abs gallery">
  <div class="tint" role="img" aria-label="Horse portrait under a gold overlay"><svg width="60" height="60" viewBox="0 0 60 60"><line x1="30" y1="4" x2="30" y2="56" stroke="#fff" stroke-width="2"/><line x1="4" y1="30" x2="56" y2="30" stroke="#fff" stroke-width="2"/></svg></div>
  <div role="img" aria-label="Rider in a helmet beside a horse in a forest" style="background:linear-gradient(180deg,#5d7a45,#3e4f34)"></div>
  <div role="img" aria-label="Rider galloping a chestnut horse on a ridge" style="background:linear-gradient(180deg,#8ab0d6,#b88b5a 60%,#7a5a38)"></div>
  <div role="img" aria-label="Rider on a horse on a forest trail" style="background:linear-gradient(180deg,#6a7a58,#9c7a56 60%,#5c4a36)"></div>
  <div role="img" aria-label="Trainer helping a young rider onto a horse" style="background:linear-gradient(180deg,#d6e0e8,#6c5a46 60%,#4a3a2c)"></div>
  <div role="img" aria-label="Rider on a horse in an open valley" style="background:linear-gradient(180deg,#b8c8d4,#8a9a8a 50%,#6b6a4e)"></div>
  <div role="img" aria-label="Show jumper clearing a red and white fence" style="background:linear-gradient(180deg,#5f8c3a,#4a7030 60%,#7a5a3a)"></div>
  <div role="img" aria-label="Riders on a misty woodland path" style="background:linear-gradient(180deg,#c8d0c0,#6a7c58 50%,#3e4a32)"></div>
</div>

<!-- question -->
<h2 class="abs section-title q-title">Have Any Question ?</h2>
<p class="abs q-text">Lorem Ipsum has been the industry's standard dummy text ever since the , when an unknown printer took</p>
<div class="field" style="top:4776px">Name *</div>
<div class="field" style="top:4836px">Email *</div>
<div class="field" style="top:4900px">Your Question ?</div>
<span class="abs btn submit">SUBMIT</span>

<!-- footer -->
<footer class="abs footer"></footer>
<div class="abs f-brand">The Wandering Mentor</div>
<div class="abs f-social" aria-label="Social links"><span></span><span></span><span></span></div>
<div class="abs f-head" style="left:336px">Sitemap</div>
<ul class="abs f-list"><li>News</li><li>Events</li><li>Gallery</li><li>Advise</li><li>Horsemanship</li><li>Dressage</li></ul>
<div class="abs f-head" style="left:612px;color:#fff">Contact Us</div>
<div class="abs f-contact">
  <div><svg width="16" height="16" viewBox="0 0 16 16"><path d="M4 2 L6.5 2 L7.5 5 L6 6.5 C7 8.5 8 9.5 10 10.5 L11.5 9 L14 10 L14 12.5 C14 13.5 13 14 12 14 C7 13.5 2.5 9 2 4 C2 3 3 2 4 2Z" fill="#d3a35c"/></svg>+1 000 000 0000</div>
  <div><svg width="16" height="12" viewBox="0 0 16 12"><rect x="1" y="1" width="14" height="10" rx="1" fill="#d3a35c"/><path d="M1 1.5 L8 7 L15 1.5" fill="none" stroke="#1e1e1e" stroke-width="1.2"/></svg>info@wanderingmentor.blog</div>
</div>
<div class="abs f-head" style="left:886px">Newsletter Signup!</div>
<p class="abs f-news">Would you like to receive our exclusive update for signup !</p>
<div class="abs f-input">Enter Email *<span><svg width="14" height="14" viewBox="0 0 14 14"><path d="M1 7 L13 1 L9 13 L7 8 Z" fill="#1e1e1e"/></svg></span></div>
<div class="abs copy">©<em>The Wandering Mentor</em> ~ 2021 All rights reserved.</div>

</body>
</html>
```